Business Card - Cooperate

Business Card for Larkfield Management Consulting

Target Market(s)

Corparte - b2B

Industry/Entity Type

Management Consulting - Professional Services

Contact Information for Business Card

Company Name , Slogan , Dummy Address,

Requirements
Must have
• Reach your Full Potential

```html
<!DOCTYPE html>
<html lang="en">
<head>
<meta charset="utf-8">
<title>Larkfield Management Consulting – Business Card</title>
<link rel="stylesheet" href="https://fonts.googleapis.com/css2?family=Open+Sans:wght@400;600;700&display=swap">
<style>
  :root {
    --page-bg: #e6e7ea;
    --card-bg: #ffffff;
    --brand-blue: #2c4a9e;
    --brand-teal: #1c9a7c;
    --accent-green: #5bb543;
    --rule-violet: #8783b5;
    --text-grey: #55585e;
    --card-shadow: 0 10px 30px rgba(0, 0, 0, 0.18);
  }
  * { box-sizing: border-box; margin: 0; padding: 0; }
  html, body {
    width: 1200px;
    height: 900px;
    overflow: hidden;
    background: var(--page-bg);
    font-family: "Open Sans", Arial, sans-serif;
  }
  .canvas {
    width: 1200px;
    height: 900px;
    display: flex;
    flex-direction: column;
    align-items: center;
    justify-content: center;
    gap: 24px;
  }
  .card {
    width: 700px;
    height: 400px;
    background: var(--card-bg);
    box-shadow: var(--card-shadow);
    position: relative;
  }

  /* Front */
  .card--front {
    display: flex;
    align-items: center;
    justify-content: center;
  }
  .brand {
    display: flex;
    align-items: center;
    gap: 18px;
  }
  .brand__dot {
    width: 62px;
    height: 62px;
    border-radius: 50%;
    background: var(--brand-blue);
    flex: none;
  }
  .brand__text {
    display: flex;
    flex-direction: column;
  }
  .brand__name {
    font-size: 58px;
    font-weight: 600;
    line-height: 1;
    color: var(--brand-blue);
    letter-spacing: 1px;
  }
  .brand__slogan {
    margin-top: 6px;
    font-size: 13px;
    font-weight: 700;
    letter-spacing: 3.4px;
    color: var(--brand-teal);
    text-transform: uppercase;
  }

  /* Back */
  .card--back {
    display: flex;
    flex-direction: column;
    align-items: center;
  }
  .back-mark {
    margin-top: 58px;
    display: flex;
    flex-direction: column;
    align-items: center;
    gap: 14px;
  }
  .back-mark__dot {
    width: 120px;
    height: 120px;
    border-radius: 50%;
    background: var(--brand-blue);
  }
  .back-mark__name {
    font-size: 34px;
    font-weight: 600;
    color: var(--brand-blue);
    letter-spacing: 1px;
  }
  .address {
    position: absolute;
    left: 70px;
    right: 70px;
    bottom: 52px;
    border-top: 1px solid var(--rule-violet);
    padding-top: 12px;
    display: flex;
    align-items: center;
    justify-content: center;
    gap: 8px;
    font-size: 17px;
    color: var(--text-grey);
  }
  .address__icon { width: 14px; height: 20px; flex: none; }
</style>
</head>
<body>
  <main class="canvas">
    <section class="card card--front" aria-label="Business card front">
      <div class="brand">
        <span class="brand__dot"></span>
        <div class="brand__text">
          <span class="brand__name">Larkfield</span>
          <span class="brand__slogan">Reach your full potential</span>
        </div>
      </div>
    </section>

    <section class="card card--back" aria-label="Business card back">
      <div class="back-mark">
        <span class="back-mark__dot"></span>
        <span class="back-mark__name">Larkfield</span>
      </div>
      <p class="address">
        <svg class="address__icon" viewBox="0 0 14 20" aria-hidden="true">
          <path d="M7 0C3.1 0 0 3.1 0 7c0 5 7 13 7 13s7-8 7-13c0-3.9-3.1-7-7-7z" fill="var(--accent-green)"/>
          <circle cx="7" cy="7" r="2.6" fill="#fff"/>
        </svg>
        11 dummy city, dummy place, P.O Box 0000 Dummy Land
      </p>
    </section>
  </main>
</body>
</html>
```